Awesome Truck Wrap Design for contractor

I have a 2020 Ravon Tundrel - Regular Cab - Long Bed

I need a wrap for my business.
Design should be simple.

Back ground should be yellow. Hood should be Green

Would like to see a simple design shapes in yellow background.
Like example below:
https://www.pixelgram.example/photo.php?fbid=583920147362819&set=pb.200084116273540.-3318630000&type=3

Slogan: You deserve the best
Phone: 555-314-6270
web: www.tallmapleworks.example

Target Market(s)

High End Homeowners

Industry/Entity Type

Roofing Contractor

Font styles to use
Sans Serif

Colors
00AB8E
00BBA5
67D7C9
C6EFE9
E9F9F6
FFC000
F8CF3A
FAE287
FDF2CF
FEFAEE

Requirements
Must have
• Design Must be simple - Easy to Read
Should not have
• Picture of roof or roof symbols like triangles

```html
<!DOCTYPE html>
<html lang="en">
<head>
<meta charset="utf-8">
<title>Tall Maple Works – Truck Wrap Side Panel</title>
<link rel="stylesheet" href="https://fonts.googleapis.com/css2?family=Poppins:wght@600;700;800&family=Barlow+Condensed:wght@500;600;700&display=swap">
<style>
  :root {
    --canvas-bg: #e8e8e8;
    --wrap-green: #1aab8a;
    --wrap-olive: #c9c24e;
    --wrap-yellow: #ffc000;
    --wrap-yellow-soft: #f8cf3a;
    --accent-green: #2f9c45;
    --ink: #2a2a2a;
    --white: #ffffff;
    --teal-line: #00ab8e;
  }
  * { margin: 0; padding: 0; box-sizing: border-box; }
  html, body {
    width: 1200px;
    height: 1035px;
    overflow: hidden;
    background: var(--canvas-bg);
  }
  .wrap-panel {
    position: absolute;
    left: 50px;
    top: 328px;
    width: 1100px;
    height: 379px;
    overflow: hidden;
    background: linear-gradient(90deg,
      var(--wrap-green) 0%,
      #7fb872 20%,
      var(--wrap-olive) 45%,
      var(--wrap-yellow-soft) 70%,
      var(--wrap-yellow) 100%);
  }
  .accent-lines {
    position: absolute;
    inset: 0;
    width: 100%;
    height: 100%;
  }
  .website {
    position: absolute;
    left: 70px;
    top: 148px;
    font-family: "Poppins", sans-serif;
    font-weight: 700;
    font-size: 18px;
    color: var(--white);
    letter-spacing: 0.2px;
  }
  .brand-name {
    position: absolute;
    left: 300px;
    top: 168px;
    display: flex;
    align-items: center;
    gap: 10px;
  }
  .brand-name .brand-square {
    width: 16px;
    height: 16px;
    background: var(--accent-green);
  }
  .brand-name .brand-text {
    font-family: "Poppins", sans-serif;
    font-weight: 800;
    font-size: 28px;
    line-height: 1.0;
    color: var(--ink);
    text-transform: uppercase;
  }
  .slogan {
    position: absolute;
    left: 572px;
    top: 164px;
    font-family: "Barlow Condensed", sans-serif;
    line-height: 0.9;
  }
  .slogan span { display: block; }
  .slogan .slogan-you { font-size: 40px; font-weight: 600; color: var(--ink); }
  .slogan .slogan-deserve { font-size: 20px; font-weight: 700; color: var(--accent-green); }
  .slogan .slogan-the { font-size: 17px; font-weight: 600; color: var(--ink); padding-left: 42px; }
  .slogan .slogan-best { font-size: 56px; font-weight: 700; color: var(--accent-green); }
  .mascot {
    position: absolute;
    left: 672px;
    top: 100px;
    width: 110px;
    height: 175px;
    border-radius: 40px 40px 12px 12px;
    background: linear-gradient(180deg, #e3a63a 0%, #d9b070 55%, #c49a5c 100%);
  }
  .phone {
    position: absolute;
    left: 800px;
    top: 122px;
    display: flex;
    align-items: center;
    gap: 4px;
    font-family: "Poppins", sans-serif;
    font-weight: 700;
    font-size: 31px;
    color: var(--ink);
  }
  .phone svg { width: 26px; height: 26px; }
</style>
</head>
<body>
  <section class="wrap-panel">
    <svg class="accent-lines" viewBox="0 0 1254 432" preserveAspectRatio="none" aria-hidden="true">
      <defs>
        <linearGradient id="stripe" x1="0" y1="1" x2="1" y2="0">
          <stop offset="0" stop-color="#00ab8e"/>
          <stop offset="1" stop-color="#ffc000"/>
        </linearGradient>
      </defs>
      <g stroke="url(#stripe)" stroke-width="4" fill="none">
        <line x1="352" y1="148" x2="484" y2="78"/>
        <line x1="172" y1="362" x2="520" y2="70" stroke-opacity="0.45"/>
        <line x1="471" y1="420" x2="800" y2="128"/>
        <line x1="640" y1="190" x2="890" y2="18"/>
        <line x1="775" y1="432" x2="1150" y2="100" stroke-opacity="0.45"/>
        <line x1="935" y1="425" x2="1205" y2="190"/>
      </g>
    </svg>

    <div class="website">www.tallmapleworks.example</div>

    <div class="brand-name">
      <div class="brand-square"></div>
      <div class="brand-text">Tall Maple<br>Works</div>
    </div>

    <div class="slogan">
      <span class="slogan-you">YOU</span>
      <span class="slogan-deserve">DESERVE</span>
      <span class="slogan-the">THE</span>
      <span class="slogan-best">BEST</span>
    </div>

    <div class="mascot" role="img" aria-label="Cartoon mascot in a cap and work uniform giving a thumbs up"></div>

    <div class="phone">
      <svg viewBox="0 0 24 24" aria-hidden="true">
        <path d="M6.6 10.8a15.1 15.1 0 0 0 6.6 6.6l2.2-2.2a1 1 0 0 1 1-.25 11.4 11.4 0 0 0 3.6.57 1 1 0 0 1 1 1V20a1 1 0 0 1-1 1A17 17 0 0 1 3 4a1 1 0 0 1 1-1h3.5a1 1 0 0 1 1 1c0 1.25.2 2.45.57 3.57a1 1 0 0 1-.25 1z" fill="none" stroke="#2a2a2a" stroke-width="2"/>
      </svg>
      <span>555-314-6270</span>
    </div>
  </section>
</body>
</html>
```